Commercial Flooring Contractor Website ($100 Bonus)

We are working with a new commercial flooring contractor in California. They work on schools, hospitals, and government projects.
A few websites for inspiration:
https://trimcoverwork.example (These guys are competitors and provide the same work our client does).
https://zqpavingsco.example (Although NOT a contractor, the simplicity of this site is stunning).
https://www.quietrapid.example (NOT a flooring contractor, but this site is modern, and has a boldness to it).
https://www.dawnfoldatelier.example/en-us (website for an Architectural office that is clean and showcases their work. I can see this working for a flooring contractor).
Thank you for taking the time to consider designing a website for us. We are web developers based in Stockton, CA, USA. Most of our projects go through the same process. Understanding this process may help you win a project with us. We custom-code all of our websites in-house. We don’t have any requirements as to what tools you use for your design, but we ask that you follow these guidelines.
IMAGES:
If you use any images or icons in the design, we ask that you have a link to the asset so we can purchase the image/icon. Most of the designs we submit do not have the customer’s images on them unless they have some great images. Be creative; show us the feeling you are trying to portray with your image choices. Use any royalty-free site you choose. We subscribe to Velto and mainly use their images, but we can purchase images outside of Velto.
FONTS:
We ask that you identify the fonts you’re using in the design. This can be done in a message if you want. We typically use Google Fonts and Velto Fonts.
CONTENT:
We're always open to different content and ideas. We often submit designs with stock images so the client can see our vision. We typically take pictures after the website launch to use their images with our vision. Lorem Ipsum is fine for paragraphs, but we ask that you make the Headers with correct English. We want to be able to show the vision and identify the sections of the website.
INSPIRATION:
We typically add a couple of links in the brief of websites we like to help you get started in your design.
REVISIONS:
We do not often ask for revisions of the designs unless we see something in the design that may not appeal to the client. If there are slight changes that we want to make, we do that in the development process.
FEEDBACK:
We rarely give feedback on designs during the design process. We are working on many website projects and do not have the time to provide feedback. We usually respond if your request is well thought out and asks specific questions, but a note asking “feedback, please” usually goes unanswered.
1 page

```html
<!DOCTYPE html>
<html lang="en">
<head>
<meta charset="utf-8">
<title>Truline Floors — Commercial Flooring</title>
<link href="https://fonts.googleapis.com/css2?family=Oswald:wght@500;600&family=Montserrat:wght@400;500;600;700&family=Pinyon+Script&display=swap" rel="stylesheet">
<style>
:root{
  --red:#e5383d;
  --red-dark:#d62f2f;
  --ink:#2b2b2b;
  --mint:#e0eee1;
  --card:#474c49;
  --footer:#262626;
  --white:#fff;
}
*{box-sizing:border-box;margin:0;padding:0}
html,body{width:1200px;height:4332px;overflow:hidden}
body{position:relative;background:var(--white);font-family:"Montserrat",sans-serif;color:var(--ink)}
.abs{position:absolute}
.photo{position:absolute;overflow:hidden}

/* hero */
.hero{position:absolute;left:0;top:0;width:1200px;height:632px;
  background:
    radial-gradient(ellipse 60% 45% at 70% 30%,rgba(255,236,180,.55),transparent 70%),
    radial-gradient(ellipse 50% 40% at 20% 70%,rgba(214,178,104,.55),transparent 70%),
    linear-gradient(180deg,#5a4a30 0%,#a88c55 38%,#c4a568 55%,#6d5a3a 80%,#2f271b 100%)}
.hero::after{content:"";position:absolute;inset:0;background:rgba(20,15,8,.22)}
.hero > *{z-index:1}
.phone{left:40px;top:12px;color:var(--white);font:500 20px "Oswald",sans-serif;display:flex;align-items:center;gap:8px}
.nav a{position:absolute;top:70px;color:var(--white);font:600 16px "Montserrat",sans-serif;text-decoration:none;letter-spacing:.5px}
.brand{left:520px;top:30px;width:160px;height:102px;display:flex;align-items:center;justify-content:center;gap:8px;color:var(--white);font:600 22px "Oswald",sans-serif;letter-spacing:1px;white-space:nowrap}
.brand .dot,.footer-brand .dot{flex:none;width:14px;height:14px;border-radius:50%;background:var(--red)}
.pill{position:absolute;border-radius:20px;font:600 15px "Montserrat",sans-serif;display:flex;align-items:center;justify-content:center;color:var(--white);letter-spacing:.4px;white-space:nowrap}
.pill.solid{background:var(--red)}
.pill.ghost{border:3px solid var(--red);background:rgba(0,0,0,.35)}
.hero-title{left:0;width:1200px;top:242px;text-align:center;color:var(--white);font:600 66px/80px "Oswald",sans-serif;letter-spacing:1px;text-shadow:0 3px 6px rgba(0,0,0,.4)}

/* section headings */
.script{position:absolute;width:100%;text-align:center;font:400 50px "Pinyon Script",cursive;color:var(--ink)}
.heading{position:absolute;width:100%;text-align:center;font:700 46px "Montserrat",sans-serif;color:var(--red);letter-spacing:2px;white-space:nowrap}

/* services */
.frame{position:absolute;border:4px solid var(--red)}
.feature{position:absolute;left:600px;height:44px;background:var(--mint);display:flex;align-items:center;gap:14px;padding-left:14px;font:500 20px "Montserrat",sans-serif;color:#333;white-space:nowrap}
.tile{position:absolute;display:flex;align-items:center;justify-content:center;color:var(--white);font:500 42px "Oswald",sans-serif;text-shadow:0 2px 6px rgba(0,0,0,.8);white-space:nowrap}

/* about */
.about-text{left:110px;width:420px;top:2565px;text-align:center;font:400 16px/25px "Montserrat",sans-serif;color:#555}

/* gallery */
.gallery{position:absolute;left:0;top:2806px;width:1200px;height:772px;
  background:radial-gradient(ellipse 40% 30% at 50% 10%,rgba(150,152,156,.5),transparent 70%),linear-gradient(180deg,#5a5c5e 0%,#35373a 35%,#2a2b2d 60%,#242528 100%)}
.view-all{left:464px;top:3461px;width:272px;height:46px;background:var(--red-dark);color:var(--white);font:500 24px "Montserrat",sans-serif;display:flex;align-items:center;justify-content:center}

/* testimonial */
.quote-card{left:234px;top:3775px;width:739px;height:232px;background:var(--card);border-radius:6px}
.avatar{left:329px;top:3794px;width:124px;height:124px;border-radius:50%;background:radial-gradient(circle at 50% 40%,#c9ccd2,#5d6f8a);border:3px solid #fff}
.person{left:291px;width:200px;text-align:center;color:#fff}
.quote{left:571px;top:3826px;width:370px;color:#fff;font:400 15px/22px "Montserrat",sans-serif}
.quote-mark{left:535px;top:3812px;color:#888;font:700 54px/1 Georgia,serif;font-style:italic}

/* footer */
.footer{position:absolute;left:0;top:4079px;width:1200px;height:253px;background:var(--footer);color:#fff}
.footer h4{position:absolute;top:42px;font:400 21px "Montserrat",sans-serif;letter-spacing:.5px}
.menu{position:absolute;left:534px;top:74px;list-style:none;font:400 13px/25px "Montserrat",sans-serif}
.footer-brand{left:40px;top:70px;width:180px;height:100px;display:flex;align-items:center;justify-content:center;gap:8px;font:600 24px "Oswald",sans-serif;letter-spacing:1px;white-space:nowrap}
.contact-row{position:absolute;left:950px;display:flex;gap:10px;font:400 13px/18px "Montserrat",sans-serif}
.rule{left:0;top:4281px;width:1200px;height:1px;background:#444}
.copyright{left:0;width:1200px;top:4296px;text-align:center;font:400 13px "Montserrat",sans-serif;color:#999}
</style>
</head>
<body>

<header class="hero" role="img" aria-label="Hotel lounge with gold patterned marble floor">
  <div class="abs phone">
    <svg width="18" height="18" viewBox="0 0 24 24"><path fill="#e5383d" d="M6.6 10.8a15 15 0 0 0 6.6 6.6l2.2-2.2c.3-.3.7-.4 1-.2 1.1.4 2.3.6 3.6.6.6 0 1 .4 1 1V20c0 .6-.4 1-1 1A17 17 0 0 1 3 4c0-.6.4-1 1-1h3.5c.6 0 1 .4 1 1 0 1.3.2 2.5.6 3.6.1.3 0 .7-.2 1z"/></svg>
    555-014-XXXX
  </div>
  <div class="pill solid" style="left:975px;top:16px;width:186px;height:30px;font-size:14px;font-weight:500">REQUEST A QUOTE</div>
  <nav class="nav">
    <a style="left:154px">HOME</a>
    <a style="left:257px">ABOUT</a>
    <a style="left:369px">SERVICES</a>
    <a style="left:736px">GALLERY</a>
    <a style="left:866px">CONTACT US</a>
  </nav>
  <div class="abs brand"><span class="dot"></span>TRULINE FLOORS</div>
  <h1 class="abs hero-title">PROFESSIONAL INDUSTRIAL CONCRETE<br>FLOORING INSTALLATIONS</h1>
  <div class="pill solid" style="left:388px;top:461px;width:200px;height:38px">REQUEST A QUOTE</div>
  <div class="pill ghost" style="left:612px;top:461px;width:200px;height:38px">CONTACT US</div>
  <svg class="abs" style="left:580px;top:556px" width="40" height="50" viewBox="0 0 40 50"><path d="M20 2v44M4 30l16 16 16-16" stroke="#ddd" stroke-width="4" fill="none"/></svg>
</header>

<!-- services -->
<div class="script" style="top:694px">Services</div>
<h2 class="heading" style="top:742px">WHAT WE DO</h2>
<div class="photo" role="img" aria-label="Businessman with laptop seated in a bright marble-floored corridor" style="left:101px;top:828px;width:420px;height:524px;background:radial-gradient(ellipse 60% 40% at 75% 75%,rgba(236,210,170,.9),transparent 70%),linear-gradient(120deg,#7c6a72 0%,#a999a0 35%,#d8c6b4 65%,#b89572 100%)"></div>
<div class="frame" style="left:146px;top:848px;width:397px;height:521px"></div>

<div class="feature" style="top:828px;width:404px"><svg width="26" height="22" viewBox="0 0 26 22"><path d="M4 18L20 4M6 4l16 14" stroke="#e5383d" stroke-width="3"/></svg>Bondability Up to 20 Million</div>
<div class="feature" style="top:888px;width:468px"><svg width="26" height="22" viewBox="0 0 26 22"><path d="M4 18L20 4M6 4l16 14" stroke="#e5383d" stroke-width="3"/></svg>Experience Modification Rate .60 – .64</div>
<div class="feature" style="top:948px;width:465px"><svg width="26" height="22" viewBox="0 0 26 22"><path d="M4 18L20 4M6 4l16 14" stroke="#e5383d" stroke-width="3"/></svg>Installers Certified for Secure Entities</div>
<div class="feature" style="top:1008px;width:465px"><svg width="26" height="22" viewBox="0 0 26 22"><path d="M4 18L20 4M6 4l16 14" stroke="#e5383d" stroke-width="3"/></svg>Overnight &amp; Weekend Work Capacity</div>
<div class="feature" style="top:1068px;width:404px"><svg width="26" height="22" viewBox="0 0 26 22"><path d="M4 18L20 4M6 4l16 14" stroke="#e5383d" stroke-width="3"/></svg>Design/Build Expertise</div>
<div class="feature" style="top:1128px;width:404px"><svg width="26" height="22" viewBox="0 0 26 22"><path d="M4 18L20 4M6 4l16 14" stroke="#e5383d" stroke-width="3"/></svg>Value-Engineering Analysis</div>
<div class="feature" style="top:1188px;width:465px"><svg width="26" height="22" viewBox="0 0 26 22"><path d="M4 18L20 4M6 4l16 14" stroke="#e5383d" stroke-width="3"/></svg>Specification &amp; Budgeting Assistance</div>
<div class="feature" style="top:1248px;width:468px"><svg width="26" height="22" viewBox="0 0 26 22"><path d="M4 18L20 4M6 4l16 14" stroke="#e5383d" stroke-width="3"/></svg>Supplier Negotiations &amp; Scaled Pricing</div>
<div class="feature" style="top:1308px;width:495px"><svg width="26" height="22" viewBox="0 0 26 22"><path d="M4 18L20 4M6 4l16 14" stroke="#e5383d" stroke-width="3"/></svg>Material Warehousing for Ongoing Jobs</div>

<div class="tile" role="img" aria-label="Open-plan office with grey carpet tiles" style="left:40px;top:1446px;width:741px;height:283px;background:radial-gradient(ellipse 45% 50% at 70% 75%,rgba(70,70,72,.7),transparent 70%),linear-gradient(180deg,#dcdedf 0%,#a9abac 45%,#7d7f81 75%,#5f6062 100%)">FLOOR FITTING</div>
<div class="tile" role="img" aria-label="Empty room with speckled coated floor" style="left:798px;top:1446px;width:361px;height:283px;background:linear-gradient(180deg,#f1f0ed 0%,#dad8d3 45%,#bdbbb6 75%,#a3a19c 100%)">COATING FLOORING</div>
<div class="tile" role="img" aria-label="Lounge with brown carpet and sofas" style="left:40px;top:1746px;width:362px;height:282px;background:radial-gradient(ellipse 60% 40% at 50% 25%,rgba(214,170,100,.8),transparent 70%),linear-gradient(180deg,#c49a5e 0%,#8f6a3d 50%,#4b3521 100%)">CARPET FLOORING</div>
<div class="tile" role="img" aria-label="Large empty hall with stone floor tiles" style="left:418px;top:1746px;width:741px;height:282px;background:linear-gradient(180deg,#e6e3de 0%,#c4bcb4 40%,#958a80 75%,#746a62 100%)">TILES FLOORING</div>
<div class="tile" role="img" aria-label="Lounge with dark wooden floor and orange sofa" style="left:40px;top:2045px;width:551px;height:283px;background:radial-gradient(ellipse 30% 25% at 25% 55%,rgba(190,90,40,.75),transparent 70%),linear-gradient(180deg,#3f4036 0%,#5e4a36 50%,#6d5138 70%,#3a2b20 100%)">WOODEN FLOORING</div>
<div class="tile" role="img" aria-label="Factory hall with glossy blue resin floor" style="left:608px;top:2045px;width:551px;height:283px;background:radial-gradient(ellipse 40% 20% at 30% 45%,rgba(70,160,90,.7),transparent 70%),linear-gradient(180deg,#e4eef6 0%,#9fc0e4 35%,#4f86d0 65%,#2456b0 100%)">RESIN FLOORING</div>

<!-- about -->
<div class="script" style="left:110px;width:420px;top:2430px">About Us</div>
<h2 class="heading" style="left:110px;width:420px;top:2490px">WHO WE ARE</h2>
<p class="abs about-text">Lorem ipsum dolor sit amet, consectetur adipiscing elit, sed do eiusmod tempor incididu ut labore et dolore magna aliqua. Quis ipsum suspendisse ultrices gravida. Risus commodo viverra maecenas accumsan lacus vel facilisis.</p>
<div class="photo" role="img" aria-label="Office with plants and light wooden floor" style="left:690px;top:2399px;width:244px;height:171px;background:radial-gradient(ellipse 50% 45% at 65% 30%,rgba(60,100,50,.85),transparent 70%),linear-gradient(180deg,#8a8a6a 0%,#c8b798 60%,#e0d4bf 100%)"></div>
<div class="frame" style="left:761px;top:2463px;width:240px;height:205px"></div>
<div class="photo" role="img" aria-label="Glazed corridor with polished white floor" style="left:825px;top:2525px;width:245px;height:208px;background:linear-gradient(180deg,#8f9599 0%,#c9cdd0 45%,#eef0f0 75%,#f7f8f8 100%)"></div>

<!-- gallery -->
<section class="gallery" role="img" aria-label="Dim corridor backdrop with dark carpet"></section>
<div class="script" style="top:2868px;color:#fff">Gallery</div>
<h2 class="heading" style="top:2924px;color:#fff">FEATURES PROJECTS</h2>
<div class="photo" role="img" aria-label="Green wall office with wooden floor" style="left:42px;top:2995px;width:267px;height:420px;background:linear-gradient(90deg,rgba(50,90,40,.6),transparent 55%),linear-gradient(180deg,#41602f 0%,#7d7656 45%,#b89f7a 75%,#cdb894 100%)"></div>
<div class="photo" role="img" aria-label="Lobby with patterned marble floor" style="left:326px;top:2995px;width:267px;height:194px;background:radial-gradient(ellipse 50% 40% at 40% 70%,rgba(230,200,140,.8),transparent 70%),linear-gradient(160deg,#d3ad66,#8c6e40 60%,#5a4830)"></div>
<div class="photo" role="img" aria-label="Glass-walled hall with white floor" style="left:610px;top:2995px;width:267px;height:194px;background:linear-gradient(180deg,#8e979d 0%,#c7cdd0 50%,#eef0f1 100%)"></div>
<div class="photo" role="img" aria-label="Reception with inlaid white floor" style="left:894px;top:2995px;width:267px;height:194px;background:linear-gradient(180deg,#a8a49c 0%,#dedbd5 45%,#f3f1ee 100%)"></div>
<div class="photo" role="img" aria-label="Circular reception desk on cream marble" style="left:326px;top:3222px;width:267px;height:193px;background:linear-gradient(180deg,#2e2a26 0%,#5a5046 35%,#c8bda6 70%,#e3dbc8 100%)"></div>
<div class="photo" role="img" aria-label="Empty warehouse with sealed concrete floor" style="left:610px;top:3222px;width:267px;height:193px;background:linear-gradient(180deg,#77756e 0%,#a19f97 45%,#c2c1bb 100%)"></div>
<div class="photo" role="img" aria-label="Long white marble corridor" style="left:894px;top:3222px;width:267px;height:193px;background:radial-gradient(ellipse 25% 40% at 50% 40%,rgba(250,250,250,.9),transparent 70%),linear-gradient(180deg,#d0d0ce,#9b9b99)"></div>
<div class="abs view-all">VIEW ALL</div>

<!-- testimonial -->
<div class="script" style="top:3640px">Testmonial</div>
<h2 class="heading" style="top:3692px;font-size:40px">WHAT OUR HAPPY CLIENTS HAVE TO SAY</h2>
<svg class="abs" style="left:138px;top:3838px" width="56" height="108" viewBox="0 0 56 108"><path d="M52 2L4 54l48 52" stroke="#333" stroke-width="4" fill="none"/></svg>
<svg class="abs" style="left:1008px;top:3838px" width="56" height="108" viewBox="0 0 56 108"><path d="M4 2l48 52-48 52" stroke="#333" stroke-width="4" fill="none"/></svg>
<div class="abs quote-card"></div>
<div class="abs avatar" role="img" aria-label="Client portrait"></div>
<div class="abs person" style="top:3930px;font:400 16px 'Montserrat',sans-serif">PERSON NAME</div>
<div class="abs person" style="top:3952px;font:400 13px 'Montserrat',sans-serif">CEO</div>
<div class="abs person" style="top:3969px;font:400 11px 'Montserrat',sans-serif">Company name</div>
<div class="abs quote-mark">“</div>
<p class="abs quote">Lorem ipsum dolor sit amet, consectetur adipiscing elit, sed do eiusmod tempor incididunt ut labore et dolore magna aliqua. Quis ipsum suspendisse ultrices gravida. Risus commodo viverra maecenas accumsan lacus vel facilisis.</p>

<!-- footer -->
<footer class="footer">
  <div class="abs footer-brand"><span class="dot"></span>TRULINE FLOORS</div>
  <h4 style="left:534px">MENU</h4>
  <ul class="menu">
    <li>- Home</li><li>- About</li><li>- Services</li><li>- Gallery</li><li>- Contact Us</li>
  </ul>
  <h4 style="left:946px">CONTACT INFO</h4>
  <div class="contact-row" style="top:76px">
    <svg width="14" height="18" viewBox="0 0 14 18"><path d="M7 0a7 7 0 0 0-7 7c0 5 7 11 7 11s7-6 7-11a7 7 0 0 0-7-7zm0 9.5A2.5 2.5 0 1 1 7 4.5a2.5 2.5 0 0 1 0 5z" fill="#fff"/></svg>
    <span>Lorem ipsum dolor sit amet,<br>consectetur adipiscing elit</span>
  </div>
  <div class="contact-row" style="top:130px">
    <svg width="14" height="14" viewBox="0 0 24 24"><path fill="#fff" d="M6.6 10.8a15 15 0 0 0 6.6 6.6l2.2-2.2c.3-.3.7-.4 1-.2 1.1.4 2.3.6 3.6.6.6 0 1 .4 1 1V20c0 .6-.4 1-1 1A17 17 0 0 1 3 4c0-.6.4-1 1-1h3.5c.6 0 1 .4 1 1 0 1.3.2 2.5.6 3.6.1.3 0 .7-.2 1z"/></svg>
    <span>555-014-XXXX</span>
  </div>
  <div class="contact-row" style="top:168px;left:970px;color:var(--red);align-items:center">
    <span>Map &amp; Directions</span>
    <svg width="42" height="10" viewBox="0 0 42 10"><path d="M0 5h40M35 1l5 4-5 4" stroke="#e5383d" stroke-width="1.5" fill="none"/></svg>
  </div>
</footer>
<div class="abs rule"></div>
<div class="abs copyright">© Truline Floors All Rights Reserved.</div>

</body>
</html>
```